Say "Velvet Crumb"! Cheesecakes that is. Needs a Web Design

Velvet Crumb LLC is a start up company based in Pickerington, Ohio. We make New York Style Cheesecakes that everyone will love. We want to start building our brand with a website that will inform the the community. Lets let them know the many mouthwatering flavors of cheesecake there are to enjoy and the 3 sizes you can dive in. Because we are small, we will only be serving locally in the Franklin and Fairfield counties. We would like to see a web design using the colors from our logo. The finished design should display a playful theme and portray comfort, desire, indulgence, and fulfillment.

Target Market(s)

Dessert Lovers

Industry/Entity Type

Food Store

Coding

Coded - Design and coding required

Number of Pages Required

5+ page

Requirements
Must have
• Everything I asked for on my web format page
Nice to have
• Colors similar to the logo

```html
<!DOCTYPE html>
<html lang="en">
<head>
<meta charset="utf-8">
<title>Velvet Crumb – Cheesecakes</title>
<link rel="stylesheet" href="https://fonts.googleapis.com/css2?family=Great+Vibes&family=Dancing+Script:wght@500&family=Rokkitt:wght@400;500&family=Open+Sans:wght@400;600&display=swap">
<style>
  :root {
    --brand-red: #b3262c;
    --brand-brown: #5a1a14;
    --salmon: #f07468;
    --price: #e4685b;
    --ink: #2a2a2a;
    --line: #e3e3e3;
    --footer-bg: #2d2d2d;
    --footer-bar: #272727;
    --footer-text: #cfcfcf;
    --white: #ffffff;
  }
  * { box-sizing: border-box; margin: 0; padding: 0; }
  html, body { width: 726px; height: 1200px; overflow: hidden; background: var(--white); }
  body { position: relative; font-family: "Open Sans", Arial, sans-serif; color: var(--ink); }

  .site-header { position: absolute; left: 0; top: 0; width: 726px; height: 94px;
    background: linear-gradient(#f5f4f4, #ffffff); }
  .brand { position: absolute; left: 0; width: 726px; top: 38px; text-align: center;
    font-family: "Rokkitt", Georgia, serif; font-weight: 500; font-size: 20px; color: var(--brand-red); }

  .main-nav { position: absolute; left: 45px; top: 104px; width: 636px; height: 46px;
    border-top: 1px solid var(--line); border-bottom: 1px solid var(--line); }
  .main-nav ul { list-style: none; display: flex; height: 100%; }
  .main-nav li { font-size: 7.5px; letter-spacing: .2px; text-transform: uppercase; color: #333;
    display: flex; align-items: center; padding: 0 14px; }
  .main-nav li.active { background: var(--brand-red); color: var(--white); padding: 0 11px; margin-top: -1px; height: 47px; }
  .search { position: absolute; right: 2px; top: 11px; width: 150px; height: 21px;
    border: 1px solid #d8d8d8; background: var(--white); }
  .search svg { position: absolute; right: 7px; top: 5px; }

  .hero { position: absolute; left: 0; top: 166px; width: 726px; height: 328px; overflow: hidden; }
  .hero-photo { position: absolute; inset: 0;
    background:
      linear-gradient(180deg, rgba(214,120,132,.55) 0%, rgba(236,190,195,.25) 22%, rgba(255,255,255,0) 42%),
      linear-gradient(90deg, #efe1cf 0%, #f3e8dc 30%, #f6f1ec 55%, #f2eeeb 100%); }
  .hero-title { position: absolute; left: 0; width: 726px; top: 52px; text-align: center;
    font-family: "Great Vibes", cursive; font-weight: 400; font-size: 38px; color: #1d1d1d; }
  .hero-tagline { position: absolute; left: 345px; top: 206px; width: 320px;
    font-family: "Dancing Script", cursive; font-size: 13.5px; line-height: 22px; color: var(--brand-brown); }
  .hero-arrow { position: absolute; top: 143px; }
  .hero-arrow.prev { left: 37px; }
  .hero-arrow.next { left: 657px; }

  .featured-title { position: absolute; left: 45px; top: 534px;
    font-family: "Rokkitt", Georgia, serif; font-weight: 400; font-size: 18px; color: #222; }
  .product { position: absolute; width: 147px; }
  .product-photo { height: 113px; border: 1px solid var(--line); background: var(--white); position: relative; }
  .product-photo span { position: absolute; left: 10px; right: 10px; top: 8px; bottom: 8px; }
  .product-info { margin-top: 7px; height: 61px; border: 1px solid var(--line); text-align: center; padding-top: 10px; }
  .price { font-family: "Rokkitt", Georgia, serif; font-size: 14px; color: var(--price); line-height: 16px; }
  .name { font-family: "Rokkitt", Georgia, serif; font-size: 11.5px; color: #222; line-height: 15px; letter-spacing: .3px; }
  .details { font-size: 7.5px; color: var(--price); letter-spacing: .4px; line-height: 13px; }
  .product.highlight .product-info { background: var(--salmon); border-color: var(--salmon); }
  .product.highlight .price, .product.highlight .name, .product.highlight .details { color: var(--white); }

  .site-footer { position: absolute; left: 0; top: 992px; width: 726px; height: 168px; background: var(--footer-bg); }
  .footer-col { position: absolute; top: 26px; }
  .footer-col h3 { font-family: "Rokkitt", Georgia, serif; font-weight: 400; font-size: 13px; color: var(--white); letter-spacing: .5px; margin-bottom: 9px; }
  .footer-col ul { list-style: none; }
  .footer-col li { font-size: 7.5px; color: var(--footer-text); line-height: 16.8px; }
  .newsletter-input { width: 150px; height: 20px; border: 1px solid #8a8a8a; font-size: 6.5px; color: #aaa; padding: 5px 7px; }
  .subscribe { width: 150px; text-align: right; font-family: "Rokkitt", Georgia, serif; font-size: 8.5px; color: var(--white); margin-top: 5px; }
  .follow { position: absolute; left: 613px; top: 116px; font-family: "Rokkitt", Georgia, serif; font-size: 13px; color: var(--white); }
  .social { position: absolute; left: 611px; top: 135px; display: flex; gap: 4px; }
  .social span { width: 18px; height: 18px; border-radius: 50%; background: #5c5c5c; }

  .footer-bar { position: absolute; left: 0; top: 1160px; width: 726px; height: 40px; background: var(--footer-bar); border-top: 1px solid #3a3a3a; }
  .copyright { position: absolute; left: 46px; top: 15px; font-size: 7px; color: var(--footer-text); }
  .pay { position: absolute; left: 530px; top: 15px; font-size: 7px; color: var(--footer-text); display: flex; align-items: center; gap: 3px; }
  .pay-label { margin-right: 9px; }
  .card { width: 22px; height: 13px; border-radius: 2px; background: #e9e9e9; color: #333;
    font-size: 4.5px; font-weight: 600; display: flex; align-items: center; justify-content: center; }
</style>
</head>
<body>
  <header class="site-header">
    <div class="brand">Velvet Crumb</div>
  </header>

  <nav class="main-nav">
    <ul>
      <li class="active">Home</li>
      <li>Flavor Page</li>
      <li>Catering Page</li>
      <li>Delivery Page</li>
      <li>Q/A Page</li>
      <li>Contact Page</li>
    </ul>
    <div class="search">
      <svg width="10" height="10" viewBox="0 0 10 10"><circle cx="4" cy="4" r="3" fill="none" stroke="#222" stroke-width="1.4"/><line x1="6.2" y1="6.2" x2="9" y2="9" stroke="#222" stroke-width="1.6"/></svg>
    </div>
  </nav>

  <section class="hero">
    <div class="hero-photo" role="img" aria-label="Cheesecake topped with fresh raspberries in front of a large faded cheesecake"></div>
    <h1 class="hero-title">Best Selling Cheesecakes..</h1>
    <p class="hero-tagline">Velvet Crumb digital bakeshop. Customers should get a glimpse at what Velvet Crumb is all about. They should quickly recognize Velvet Crumb's best selling cheesecakes.</p>
    <svg class="hero-arrow prev" width="33" height="33" viewBox="0 0 33 33"><circle cx="16.5" cy="16.5" r="15" fill="#fff" fill-opacity=".5" stroke="#333" stroke-width="2.4"/><polyline points="19,10 12.5,16.5 19,23" fill="none" stroke="#333" stroke-width="2.6"/></svg>
    <svg class="hero-arrow next" width="33" height="33" viewBox="0 0 33 33"><circle cx="16.5" cy="16.5" r="15" fill="#fff" fill-opacity=".5" stroke="#333" stroke-width="2.4"/><polyline points="14,10 20.5,16.5 14,23" fill="none" stroke="#333" stroke-width="2.6"/></svg>
  </section>

  <h2 class="featured-title">Featured Products</h2>

  <article class="product highlight" style="left:45px;top:566px">
    <div class="product-photo"><span role="img" aria-label="Caramel and cherry topped cheesecake" style="background:linear-gradient(#fff,#f1e2cf 40%,#fff)"></span></div>
    <div class="product-info"><div class="price">$49.00</div><div class="name">Cheese Cake</div><div class="details">details</div></div>
  </article>
  <article class="product" style="left:208px;top:566px">
    <div class="product-photo"><span role="img" aria-label="Whipped cream topped caramel cheesecake" style="background:linear-gradient(#fff,#f5e8cc 45%,#fff)"></span></div>
    <div class="product-info"><div class="price">$49.00</div><div class="name">Cheese Cake</div><div class="details">details</div></div>
  </article>
  <article class="product" style="left:371px;top:566px">
    <div class="product-photo"><span role="img" aria-label="Crumb topped cheesecake" style="background:linear-gradient(#fff,#f1dfc6 45%,#fff)"></span></div>
    <div class="product-info"><div class="price">$49.00</div><div class="name">Cheese Cake</div><div class="details">details</div></div>
  </article>
  <article class="product" style="left:534px;top:566px">
    <div class="product-photo"><span role="img" aria-label="Chocolate chip cheesecake" style="background:linear-gradient(#fff,#f1ece0 45%,#fff)"></span></div>
    <div class="product-info"><div class="price">$49.00</div><div class="name">Cheese Cake</div><div class="details">details</div></div>
  </article>

  <article class="product" style="left:45px;top:770px">
    <div class="product-photo"><span role="img" aria-label="Cookies and cream cheesecake" style="background:linear-gradient(#fff,#ece7da 45%,#fff)"></span></div>
    <div class="product-info"><div class="price">$49.00</div><div class="name">Cheese Cake</div><div class="details">details</div></div>
  </article>
  <article class="product" style="left:208px;top:770px">
    <div class="product-photo"><span role="img" aria-label="Mixed berry topped cheesecake" style="background:linear-gradient(#fff,#ecd2d6 40%,#fff)"></span></div>
    <div class="product-info"><div class="price">$49.00</div><div class="name">Cheese Cake</div><div class="details">details</div></div>
  </article>
  <article class="product" style="left:371px;top:770px">
    <div class="product-photo"><span role="img" aria-label="Strawberry shortcake cheesecake" style="background:linear-gradient(#fff,#f4dcd8 45%,#fff)"></span></div>
    <div class="product-info"><div class="price">$49.00</div><div class="name">Cheese Cake</div><div class="details">details</div></div>
  </article>
  <article class="product" style="left:534px;top:770px">
    <div class="product-photo"><span role="img" aria-label="Golden crumb cheesecake" style="background:linear-gradient(#fff,#f2dfc0 45%,#fff)"></span></div>
    <div class="product-info"><div class="price">$49.00</div><div class="name">Cheese Cake</div><div class="details">details</div></div>
  </article>

  <footer class="site-footer">
    <div class="footer-col" style="left:45px">
      <h3>information</h3>
      <ul><li>About Us</li><li>Customer Service</li><li>Privacy Policy</li><li>Site Map</li><li>Orders and Returns</li><li>Contact Us</li></ul>
    </div>
    <div class="footer-col" style="left:200px">
      <h3>why buy from us</h3>
      <ul><li>Shipping &amp; Returns</li><li>Secure Shopping</li><li>International Shipping</li><li>Affiliates</li><li>Group Sales</li></ul>
    </div>
    <div class="footer-col" style="left:372px">
      <h3>my account</h3>
      <ul><li>Sign In</li><li>View Cart</li><li>My Wishlist</li><li>Track My Order</li><li>Help</li></ul>
    </div>
    <div class="footer-col" style="left:529px">
      <h3>newsletter</h3>
      <div class="newsletter-input">Enter your email address</div>
      <div class="subscribe">› subscribe</div>
    </div>
    <div class="follow">follow us</div>
    <div class="social"><span></span><span></span><span></span></div>
  </footer>

  <div class="footer-bar">
    <div class="copyright">© 2015 Yoursite. All Rights Reserved.</div>
    <div class="pay">
      <span class="pay-label">Pay Through</span>
      <span class="card">Vexa</span><span class="card">Mondo</span><span class="card">Amplo</span><span class="card">PayLeaf</span>
    </div>
  </div>
</body>
</html>
```